Poster for International workers day 2021 ( May day 1 )

We're looking for poster for for ( International workers day 2021 - May day ) to post on LinkedIn and insta with our company logo and content, I have attached our logo in .png format and sample content for the poster.

```html
<!DOCTYPE html>
<html lang="en">
<head>
<meta charset="UTF-8">
<title>International Workers' Day Poster</title>
<link rel="stylesheet" href="https://fonts.googleapis.com/css2?family=Jost:wght@500;600;700&family=Montserrat:ital,wght@1,300&display=swap">
<style>
  :root {
    --bg-top: #0a7598;
    --bg-mid: #175a78;
    --bg-bottom: #0d1d32;
    --white: #ffffff;
    --green: #8dc63f;
    --sky: #8ed3e0;
  }
  * { margin: 0; padding: 0; box-sizing: border-box; }
  html, body { width: 849px; height: 1200px; overflow: hidden; }
  body { background: var(--bg-bottom); }
  .poster {
    position: relative;
    width: 849px;
    height: 1200px;
    overflow: hidden;
    font-family: "Jost", sans-serif;
    color: var(--white);
  }
  .poster__backdrop {
    position: absolute;
    inset: 0;
    background: linear-gradient(180deg, var(--bg-top) 0%, var(--bg-mid) 45%, var(--bg-bottom) 100%);
  }
  .poster__frame {
    position: absolute;
    left: 54px;
    top: 54px;
    width: 741px;
    height: 1092px;
    border: 7px solid var(--white);
  }
  .headline {
    position: absolute;
    top: 154px;
    left: 0;
    width: 100%;
    text-align: center;
    font-weight: 700;
    font-size: 62px;
    line-height: 1;
    letter-spacing: 0.5px;
  }
  .occasion {
    position: absolute;
    top: 274px;
    left: 0;
    width: 100%;
    text-align: center;
    font-weight: 500;
    font-size: 43px;
    line-height: 1;
    letter-spacing: -1.6px;
    white-space: nowrap;
    color: var(--green);
  }
  .date-row {
    position: absolute;
    top: 334px;
    left: 0;
    width: 100%;
    height: 64px;
  }
  .date-row__rule {
    position: absolute;
    top: 31px;
    height: 2px;
    background: var(--white);
  }
  .date-row__rule--left { left: 132px; width: 183px; }
  .date-row__rule--right { left: 533px; width: 184px; }
  .date-row__text {
    position: absolute;
    left: 0;
    width: 100%;
    top: 2px;
    text-align: center;
    font-weight: 500;
    font-size: 66px;
    line-height: 64px;
    letter-spacing: -2.5px;
    color: var(--sky);
    padding-left: 6px;
  }
  .quote-mark {
    position: absolute;
    width: 40px;
    height: 32px;
  }
  .quote-mark--open { left: 132px; top: 541px; }
  .quote-mark--close { left: 679px; top: 779px; }
  .quote {
    position: absolute;
    top: 582px;
    left: 0;
    width: 849px;
    text-align: center;
    font-family: "Montserrat", sans-serif;
    font-style: italic;
    font-weight: 300;
    font-size: 38px;
    line-height: 48px;
    letter-spacing: 1.6px;
    padding-left: 2px;
    white-space: nowrap;
  }
  .brand {
    position: absolute;
    top: 1014px;
    left: 0;
    width: 100%;
    text-align: center;
    font-weight: 700;
    font-size: 48px;
    line-height: 1;
    letter-spacing: 2px;
    color: var(--green);
  }
</style>
</head>
<body>
  <main class="poster">
    <div class="poster__backdrop" role="img" aria-label="Blue gradient background with a faint pattern of film, camera, music and theatre icons"></div>
    <div class="poster__frame"></div>

    <h1 class="headline">Let's Celebrate</h1>
    <h2 class="occasion">INTERNATIONAL WORKER'S DAY</h2>

    <div class="date-row">
      <span class="date-row__rule date-row__rule--left"></span>
      <p class="date-row__text">1 MAY</p>
      <span class="date-row__rule date-row__rule--right"></span>
    </div>

    <svg class="quote-mark quote-mark--open" viewBox="0 0 40 32" aria-hidden="true">
      <path fill="#ffffff" d="M14 2 C6 7 2 14 3 22 C3 28 8 31 12 29 C16 27 16 21 12 19 C9 18 8 19 8 19 C8 12 11 7 16 4 Z"/>
      <path fill="#ffffff" d="M35 2 C27 7 23 14 24 22 C24 28 29 31 33 29 C37 27 37 21 33 19 C30 18 29 19 29 19 C29 12 32 7 37 4 Z"/>
    </svg>

    <p class="quote">The success of each entity<br>and organization is<br>because of the people<br>who work hard together.</p>

    <svg class="quote-mark quote-mark--close" viewBox="0 0 40 32" aria-hidden="true">
      <path fill="#ffffff" d="M26 30 C34 25 38 18 37 10 C37 4 32 1 28 3 C24 5 24 11 28 13 C31 14 32 13 32 13 C32 20 29 25 24 28 Z"/>
      <path fill="#ffffff" d="M5 30 C13 25 17 18 16 10 C16 4 11 1 7 3 C3 5 3 11 7 13 C10 14 11 13 11 13 C11 20 8 25 3 28 Z"/>
    </svg>

    <p class="brand">MIRVELQA</p>
  </main>
</body>
</html>
```